Brenmore Timber Co website design

I have created an attached txt document with specifics of what I am looking for. The short version is that I am looking for a website design for a lumber yard/building materials store. They currently do not have a website other than a simple place holder. I have included several example websites of his direct competitors as well as made a note as to which one is the best example and the design he really likes. The txt document goes in depth as to navigation, points of interest and contact information. Unfortunately like most clients the logo files sucks. I am not sure why people don't have a good logo file.

```html
<!DOCTYPE html>
<html lang="en">
<head>
<meta charset="utf-8">
<title>Brenmore Timber Co</title>
<link href="https://fonts.googleapis.com/css2?family=Open+Sans:wght@400;600;700&display=swap" rel="stylesheet">
<style>
:root{
  --green:#1f6d23;
  --green-mid:#3b8a37;
  --green-light:#4f9c45;
  --brown:#5a2a0d;
  --ink:#2b2b2b;
  --muted:#555;
  --white:#fff;
  --black:#050505;
}
*{box-sizing:border-box;margin:0;padding:0}
html,body{width:1200px;height:3560px;overflow:hidden}
body{font-family:"Open Sans",sans-serif;color:var(--ink);background:#fff;position:relative}
.abs{position:absolute}
a{color:inherit}

.topbar{left:0;top:0;width:1200px;height:50px;background:var(--green);color:#fff;font-size:14px}
.topbar .addr{left:113px;top:14px;display:flex;gap:10px;align-items:center}
.topbar .phone{right:113px;top:14px;display:flex;gap:10px;align-items:center}

.header{left:0;top:50px;width:1200px;height:92px;background:#fff}
.brand{left:110px;top:30px;width:140px;text-align:center;color:var(--green);font-weight:700;font-size:14px;line-height:1.15;display:flex;align-items:center;gap:6px}
.brand .dot{width:14px;height:14px;background:var(--brown);flex:none}
.nav{left:328px;top:32px;display:flex;gap:37px;font-size:15px;color:#222}
.nav span.active{border-bottom:2px solid var(--green);padding-bottom:4px}
.quote{left:928px;top:22px;width:160px;height:42px;background:var(--green);color:#fff;font-size:15px;display:flex;align-items:center;justify-content:center;letter-spacing:.3px}

.hero{left:0;top:142px;width:1200px;height:580px}
.hero-photo{position:absolute;inset:0;background:linear-gradient(100deg,#6a3a1e 0%,#9c6a42 30%,#7b6a5a 55%,#8c7760 75%,#5d4a3b 100%)}
.hero-title{left:110px;top:145px;color:#fff;font-size:48px;font-weight:700;line-height:1.28}
.hero-text{left:111px;top:275px;width:545px;color:#fff;font-size:14px;line-height:1.6}
.hero-btn{left:110px;top:376px;width:195px;height:60px;border:2px solid #fff;color:#fff;font-size:19px;font-weight:600;display:flex;align-items:center;justify-content:center}

.about-title{left:113px;top:785px;font-size:31px;font-weight:700;color:var(--brown)}
.about-text{left:111px;top:845px;width:441px;font-size:17px;line-height:1.33;text-align:justify;color:#333}
.btn-green{background:var(--green);color:#fff;display:flex;align-items:center;justify-content:center;font-size:17px}
.about-btn{left:111px;top:1065px;width:148px;height:45px}
.frame{background:var(--green)}
.about-photo{left:636px;top:778px;width:453px;height:335px;background:linear-gradient(160deg,#a98a60,#cfc6b6 55%,#e6e2dc);box-shadow:0 4px 10px rgba(0,0,0,.25)}

.services{left:0;top:1237px;width:1200px;height:621px;background:linear-gradient(180deg,#3d8b38,#4c9a43 50%,#3a8535)}
.sec-title{width:1200px;left:0;text-align:center;font-size:31px;font-weight:700}
.sec-sub{left:200px;width:800px;text-align:center;font-size:17px;line-height:1.6}
.services .sec-title{top:50px;color:#fff}
.services .sec-sub{top:115px;color:#fff;font-weight:600}
.svc{top:230px;width:256px;text-align:center;color:#fff}
.svc .ring{width:204px;height:204px;margin:0 auto;border:4px solid #fff;border-radius:50%;padding:14px}
.svc .pic{width:100%;height:100%;border-radius:50%}
.svc h3{margin-top:44px;font-size:27px;font-weight:700}
.svc p{margin-top:10px;font-size:20px}

.products{left:0;top:1858px;width:1200px;height:682px;background:linear-gradient(180deg,#fff 0%,#f4f8ee 55%,#cfe5a5 86%,#8fbf55 89%)}
.floor{left:0;top:2465px;width:1200px;height:75px;background:linear-gradient(180deg,#6b4327,#9a6a44 40%,#7a4c2c)}
.products .sec-title{top:70px;color:var(--brown)}
.products .sec-sub{top:140px;color:#222}
.card{top:2089px;width:319px;height:374px;background:#fff;text-align:center}
.card .pic{height:184px}
.card h3{margin-top:12px;font-size:27px;font-weight:600;color:var(--green)}
.card p{margin:8px 18px 0;font-size:15px;line-height:1.42;color:#333}
.card a{display:inline-block;margin-top:8px;font-size:16px;font-weight:700;color:var(--green)}
.card.featured{background:var(--green)}
.card.featured h3,.card.featured p,.card.featured a{color:#fff}

.resources .sec-title{top:2607px;color:var(--green)}
.resources .sec-sub{top:2677px;color:#555}
.tile{top:2776px;width:236px;height:204px;border-radius:6px}
.tile .label{position:absolute;left:20px;top:28px;color:#fff}
.tile .label b{display:block;font-size:21px;line-height:1.3}
.tile .label span{display:block;margin-top:10px;font-size:16px;line-height:1.7}
.arrow{position:absolute;left:50%;bottom:-22px;margin-left:-23px;width:46px;height:46px;border-radius:50%;background:var(--green);border:2px solid #fff;display:flex;align-items:center;justify-content:center}

.footer-bg{left:0;top:3060px;width:1200px;height:500px}
.f-brand{left:113px;top:3240px;color:#fff;font-weight:700;font-size:18px;line-height:1.2;text-align:center;width:170px}
.f-desc{left:113px;top:3300px;width:230px;color:#fff;font-size:17px;line-height:1.55}
.social{left:122px;top:3386px;display:flex;gap:12px}
.social span{width:36px;height:36px;border:2px solid #fff;border-radius:50%}
.f-head{top:3177px;color:#fff;font-size:18px;font-weight:700}
.f-head::first-letter{color:#3fa33a}
.f-list{color:#fff;font-size:18px;list-style:none}
.f-list li{display:flex;align-items:center;gap:14px;height:33px}
.f-list li::before{content:"";width:7px;height:7px;border-right:1.5px solid #fff;border-top:1.5px solid #fff;transform:rotate(45deg)}
.f-contact{left:788px;color:#fff;font-size:18px;line-height:1.33;display:flex;gap:20px}
.f-contact svg{flex:none;margin-top:3px}
.rule{left:112px;top:3470px;width:977px;height:1px;background:#bbb}
.copy{left:0;top:3500px;width:1200px;text-align:center;color:#fff;font-size:17px}
</style>
</head>
<body>

<div class="abs topbar">
  <div class="abs addr">
    <svg width="15" height="12" viewBox="0 0 15 12"><rect x="1" y="1" width="13" height="10" fill="none" stroke="#fff" stroke-width="1.4"/><path d="M1 1l6.5 5L14 1" fill="none" stroke="#fff" stroke-width="1.4"/></svg>
    Brenmore Timber Co 4810 Alder Ridge Rd, Pine Hollow, MN
  </div>
  <div class="abs phone">
    <svg width="13" height="13" viewBox="0 0 24 24"><path fill="#fff" d="M6.6 10.8a15 15 0 006.6 6.6l2.2-2.2c.3-.3.7-.4 1-.2 1.1.4 2.3.6 3.6.6.6 0 1 .4 1 1V20c0 .6-.4 1-1 1A17 17 0 013 4c0-.6.4-1 1-1h3.5c.6 0 1 .4 1 1 0 1.3.2 2.5.6 3.6.1.3 0 .7-.2 1z"/></svg>
    +1 (555) 014-2290
  </div>
</div>

<header class="abs header">
  <div class="abs brand"><span class="dot"></span><span>BRENMORE TIMBER COMPANY</span></div>
  <nav class="abs nav"><span class="active">Home</span><span>Product</span><span>Services</span><span>Company</span><span>Resources</span><span>Contact</span></nav>
  <div class="abs quote">GET A QUOTE</div>
</header>

<section class="abs hero">
  <div class="hero-photo" role="img" aria-label="Stacks of sawn lumber under a warehouse roof"></div>
  <h1 class="abs hero-title">Welcome to<br>Brenmore Timber</h1>
  <p class="abs hero-text">Lorem ipsum dolor sit amet, consectetur adipiscing elit, sed do eiusmod tempor incididunt ut labore et dolore magna aliqua. Ut enim ad minim veniam, quis nostrud exercitation ullamco laboris nisi ut aliquip ex ea commodo consequat.</p>
  <div class="abs hero-btn">Get Started</div>
</section>

<svg class="abs" style="left:0;top:620px" width="1200" height="110" viewBox="0 0 1200 110">
  <path d="M0 15 L1088 100 L1200 22 L1200 110 L0 110Z" fill="#fff"/>
  <path d="M0 15 L1088 100 L1200 22 L1200 30 L1090 95 L0 22Z" fill="#1f6d23"/>
  <path d="M0 22 L1090 95 L1200 30 L1200 40 L1088 100 L0 30Z" fill="#fff"/>
</svg>

<h2 class="abs about-title">About Us</h2>
<p class="abs about-text">Sed ut perspiciatis unde omnis iste natus error sit voluptatem accusantium doloremque laudantium, totam rem aperiam, eaque ipsa quae ab illo inventore veritatis et quasi architecto beatae vitae dicta sunt explicabo. Nemo enim ipsam voluptatem quia voluptas sit aspernatur aut odit aut fugit, sed quia consequuntur magni dolores eos qui ratione voluptatem sequi nesciunt,</p>
<div class="abs btn-green about-btn">Read More</div>
<div class="abs frame" style="left:925px;top:762px;width:182px;height:135px"></div>
<div class="abs frame" style="left:617px;top:995px;width:181px;height:137px"></div>
<div class="abs about-photo" role="img" aria-label="Staff working at the counter inside the store office"></div>

<section class="abs services">
  <h2 class="abs sec-title">Our Services</h2>
  <p class="abs sec-sub">sed quia non numquam eius modi tempora incidunt ut labore et dolore magnam aliquam quaerat voluptatem. Ut enim ad minima veniam,</p>
  <div class="abs svc" style="left:86px"><div class="ring"><div class="pic" role="img" aria-label="Cut log ends stacked" style="background:radial-gradient(#e2b77a,#9c6a3a)"></div></div><h3>Duis aute irure</h3><p>from $26.000</p></div>
  <div class="abs svc" style="left:342px"><div class="ring"><div class="pic" role="img" aria-label="Wooden deck on a house" style="background:linear-gradient(180deg,#7fb1e0 0%,#8a9a82 45%,#b27a4a 70%)"></div></div><h3>Nemo enim</h3><p>from $20.000</p></div>
  <div class="abs svc" style="left:599px"><div class="ring"><div class="pic" role="img" aria-label="Stacked lumber boards" style="background:linear-gradient(90deg,#b3703d,#d9a36a,#9a5f32)"></div></div><h3>Neque porro</h3><p>from $28.000</p></div>
  <div class="abs svc" style="left:855px"><div class="ring"><div class="pic" role="img" aria-label="Yard worker standing by lumber racks" style="background:linear-gradient(135deg,#4a3a2e,#8a6e52 50%,#2d3f6a)"></div></div><h3>Lorem ipsum</h3><p>from $30.000</p></div>
</section>

<section class="abs products">
  <h2 class="abs sec-title">Our Products</h2>
  <p class="abs sec-sub">sed quia non numquam eius modi tempora incidunt ut labore et dolore magnam aliquam quaerat voluptatem. Ut enim ad minima veniam,</p>
</section>
<div class="abs floor" role="img" aria-label="Wooden plank floor"></div>
<div class="abs card" style="left:112px"><div class="pic" role="img" aria-label="Store building with trucks parked out front" style="background:linear-gradient(180deg,#a8afb8,#6d665a 60%,#9b9080)"></div><h3>Lumber</h3><p>sed quia non numquam eius modi tempora incidunt ut labore et dolore magnam aliquam quaerat voluptatem. Ut enim ad minima</p><a>Read More</a></div>
<div class="abs card featured" style="left:441px"><div class="pic" role="img" aria-label="Delivery trucks in the lumber yard" style="background:linear-gradient(180deg,#b4bcc4,#7d7f74 55%,#9b978c)"></div><h3>Commercial</h3><p>sed quia non numquam eius modi tempora incidunt ut labore et dolore magnam aliquam quaerat voluptatem. Ut enim ad minima</p><a>Read More</a></div>
<div class="abs card" style="left:770px"><div class="pic" role="img" aria-label="Open storage shed with lumber" style="background:linear-gradient(180deg,#8fa0b5,#3f3a36 45%,#8a7f70)"></div><h3>Doors</h3><p>sed quia non numquam eius modi tempora incidunt ut labore et dolore magnam aliquam quaerat voluptatem. Ut enim ad minima</p><a>Read More</a></div>

<section class="resources">
  <h2 class="abs sec-title">Resources Center</h2>
  <p class="abs sec-sub">sed quia non numquam eius modi tempora incidunt ut labore et dolore magnam aliquam quaerat voluptatem. Ut enim ad minima veniam,</p>
</section>
<div class="abs tile" style="left:112px;background:linear-gradient(135deg,#3a3a3a,#6a6058)" role="img" aria-label="Dim workshop interior"><div class="label"><b>Nemo enim<br>ipsam</b><span>Duis aute irure dolor in<br>reprehenderit in voluptate</span></div><div class="arrow"><svg width="14" height="18" viewBox="0 0 14 18"><path d="M4 2l7 7-7 7" fill="none" stroke="#fff" stroke-width="2.5"/></svg></div></div>
<div class="abs tile" style="left:357px;background:linear-gradient(180deg,#c9cdd0,#b58b5c 60%,#8c6a45)" role="img" aria-label="Warehouse aisle with stacked timber"><div class="arrow"><svg width="14" height="18" viewBox="0 0 14 18"><path d="M4 2l7 7-7 7" fill="none" stroke="#fff" stroke-width="2.5"/></svg></div></div>
<div class="abs tile" style="left:604px;background:linear-gradient(90deg,#e8e6e2,#b89c80 45%,#d8cfc4)" role="img" aria-label="Room with timber wall panelling"><div class="arrow"><svg width="14" height="18" viewBox="0 0 14 18"><path d="M4 2l7 7-7 7" fill="none" stroke="#fff" stroke-width="2.5"/></svg></div></div>
<div class="abs tile" style="left:850px;background:linear-gradient(90deg,#7a8a5a,#8a6a48 50%,#c4935a)" role="img" aria-label="Pile of cut logs in a forest"><div class="arrow"><svg width="14" height="18" viewBox="0 0 14 18"><path d="M4 2l7 7-7 7" fill="none" stroke="#fff" stroke-width="2.5"/></svg></div></div>

<svg class="abs footer-bg" width="1200" height="500" viewBox="0 0 1200 500">
  <path d="M0 80 L120 18 L1200 90 L1200 500 L0 500Z" fill="#1f6d23"/>
  <path d="M0 90 L120 30 L1200 100 L1200 500 L0 500Z" fill="#050505"/>
</svg>

<div class="abs f-brand">BRENMORE TIMBER<br>COMPANY</div>
<p class="abs f-desc">Duis aute irure dolor in reprehenderit in voluptate</p>
<div class="abs social"><span></span><span></span><span></span></div>

<h4 class="abs f-head" style="left:388px">Quick Links</h4>
<ul class="abs f-list" style="left:388px;top:3235px"><li>Home</li><li>Products</li><li>Services</li><li>Company</li><li>Resources</li><li>Contact</li></ul>

<h4 class="abs f-head" style="left:582px">Company</h4>
<ul class="abs f-list" style="left:582px;top:3235px"><li>Company Info</li><li>Careers</li><li>Policies</li></ul>
<h4 class="abs f-head" style="left:582px;top:3361px">Opening hours</h4>
<div class="abs" style="left:582px;top:3405px;color:#fff;font-size:18px;display:flex;gap:14px;align-items:center"><svg width="14" height="14" viewBox="0 0 14 14"><circle cx="7" cy="7" r="6" fill="none" stroke="#3fa33a" stroke-width="1.5"/><path d="M7 3.5V7h3" fill="none" stroke="#3fa33a" stroke-width="1.5"/></svg>6:00AM-5:00PM</div>

<h4 class="abs f-head" style="left:788px">Contact</h4>
<div class="abs f-contact" style="top:3238px"><svg width="12" height="16" viewBox="0 0 12 16"><path d="M6 0a6 6 0 016 6c0 4-6 10-6 10S0 10 0 6a6 6 0 016-6z" fill="#fff"/><circle cx="6" cy="6" r="2" fill="#050505"/></svg><span>Brenmore Timber Co<br>4810 Alder Ridge Rd,<br>Pine Hollow, MN<br>55000</span></div>
<div class="abs f-contact" style="top:3362px"><svg width="16" height="16" viewBox="0 0 24 24"><path fill="#fff" d="M6.6 10.8a15 15 0 006.6 6.6l2.2-2.2c.3-.3.7-.4 1-.2 1.1.4 2.3.6 3.6.6.6 0 1 .4 1 1V20c0 .6-.4 1-1 1A17 17 0 013 4c0-.6.4-1 1-1h3.5c.6 0 1 .4 1 1 0 1.3.2 2.5.6 3.6.1.3 0 .7-.2 1z"/></svg><span>(555) 014-2290</span></div>
<div class="abs f-contact" style="top:3407px"><svg width="18" height="14" viewBox="0 0 15 12"><rect x="1" y="1" width="13" height="10" fill="none" stroke="#fff" stroke-width="1.4"/><path d="M1 1l6.5 5L14 1" fill="none" stroke="#fff" stroke-width="1.4"/></svg><span>info@brenmoretimber.com</span></div>

<div class="abs rule"></div>
<p class="abs copy">copyrights 2022 Brenmore Timber Company &nbsp;|&nbsp; All Rights Reserved</p>

</body>
</html>
```